Small boutique multi-family apartment developer needs premium website design.

We are a growing real estate development company specializing in multi family apartment development. Our company Brindel Asset Development focuses on passive real estate investors looking to maximize their current real estate portfolio by allowing us to develop and reposition their current properties allowing them more cashflow while we are also able to take over the management of their asset in order to ensure optimal performance on a consistent basis.

```html
<!DOCTYPE html>
<html lang="en">
<head>
<meta charset="utf-8">
<title>Brindel Asset Development</title>
<link href="https://fonts.googleapis.com/css2?family=Audiowide&family=Montserrat:wght@600;700&family=Open+Sans:wght@400;600&family=Poppins:wght@400;500;600&display=swap" rel="stylesheet">
<style>
:root{
  --blue:#4a7fe0;
  --blue-deep:#2f5fb8;
  --band:#345fae;
  --card:#6296e8;
  --navy:#17223a;
  --footer:#4a78c8;
  --ink:#333;
  --muted:#666;
  --white:#fff;
  --haze:#eef1f5;
}
*{margin:0;padding:0;box-sizing:border-box}
html,body{width:1200px;height:2929px;overflow:hidden;background:var(--white)}
body{position:relative;font-family:"Open Sans",sans-serif;color:var(--ink)}
.abs{position:absolute}
/* header */
.site-header{position:absolute;left:0;top:0;width:1200px;height:71px;background:var(--white)}
.brand{left:141px;top:20px;font-family:"Poppins",sans-serif;font-weight:600;font-size:19px;color:var(--blue);line-height:30px}
.nav a{position:absolute;top:26px;font-family:"Poppins",sans-serif;font-size:13.5px;color:#333;text-decoration:none}
.btn-contact{left:965px;top:18px;width:94px;height:34px;background:var(--blue);color:#fff;border-radius:6px;font-family:"Poppins",sans-serif;font-weight:600;font-size:13.5px;display:flex;align-items:center;justify-content:center}
/* hero */
.hero{left:0;top:71px;width:1200px;height:600px;overflow:hidden}
.hero-title{left:142px;top:187px;font-family:"Audiowide",sans-serif;font-size:30.5px;line-height:47px;color:#fff;letter-spacing:.3px;white-space:nowrap}
.hero-sub{left:142px;top:291px;width:370px;font-family:"Poppins",sans-serif;font-weight:500;font-size:13.5px;line-height:19px;color:#fff}
.btn-read{left:142px;top:367px;width:110px;height:34px;background:#fff;border-radius:8px;font-family:"Poppins",sans-serif;font-weight:600;font-size:13px;color:var(--blue);display:flex;align-items:center;justify-content:center}
/* team */
.team-backdrop{left:109px;top:731px;width:189px;height:120px;background:var(--haze)}
.team-photo{left:201px;top:761px;width:345px;height:330px;border-radius:40px 40px 0 40px;border:4px solid var(--blue);background:linear-gradient(135deg,#e7e3dc,#c9c2b5 55%,#7f8794)}
.h2{font-family:"Montserrat",sans-serif;font-weight:700;font-size:29px;color:var(--blue-deep)}
.team-title{left:670px;top:817px}
.team-text{left:672px;top:873px;width:392px;font-size:12.7px;line-height:22.6px;color:var(--muted);text-align:justify}
.btn-square{left:671px;top:994px;width:130px;height:39px;background:var(--blue);color:#fff;font-size:13px;display:flex;align-items:center;justify-content:center}
/* expertise */
.expertise{left:0;top:1157px;width:1200px;height:472px;background:var(--band);overflow:hidden}
.exp-title{left:141px;top:1325px;font-family:"Montserrat",sans-serif;font-weight:700;font-size:27.5px;line-height:34px;color:#fff;white-space:nowrap}
.exp-text{left:143px;top:1413px;width:378px;font-size:12.8px;line-height:22.6px;color:#fff;text-align:justify}
.service-card{position:absolute;width:159px;height:120px;background:var(--card);box-shadow:0 4px 14px rgba(20,40,90,.25);display:flex;align-items:center;justify-content:center}
.service-label{position:absolute;width:180px;text-align:center;font-size:13.3px;line-height:18px;color:#fff}
/* portfolio */
.pf-title{left:0;top:1712px;width:1190px;text-align:center;color:var(--blue)}
.pf-text{left:0;top:1764px;width:1200px;text-align:center;font-size:13px;line-height:23px;color:#777}
.photo{position:absolute;border-radius:12px}
.arrow{position:absolute;width:34px;height:34px;border-radius:50%;background:var(--blue);display:flex;align-items:center;justify-content:center}
/* cta */
.cta{left:0;top:2278px;width:1200px;height:305px;background:linear-gradient(180deg,#1a253f 0%,#1c2a48 55%,#2b3550 80%,#1f2840 100%)}
.cta-title{left:0;top:2356px;width:1200px;text-align:center;font-family:"Montserrat",sans-serif;font-weight:700;font-size:29px;color:#fff}
.cta-text{left:0;top:2410px;width:1200px;text-align:center;font-size:13.3px;color:#fff}
.btn-pill{left:514px;top:2457px;width:176px;height:38px;border-radius:20px;background:var(--blue);color:#fff;font-size:13px;display:flex;align-items:center;justify-content:center}
/* footer */
.site-footer{left:0;top:2583px;width:1200px;height:346px;background:var(--footer);overflow:hidden}
.footer-brand{left:154px;top:2688px;font-family:"Poppins",sans-serif;font-weight:600;font-size:24px;line-height:34px;color:#fff;white-space:nowrap}
.f-head{position:absolute;font-family:"Montserrat",sans-serif;font-weight:700;font-size:16.5px;color:#fff}
.f-link{position:absolute;left:699px;font-size:14.5px;color:#fff}
.f-label{position:absolute;left:886px;font-family:"Montserrat",sans-serif;font-weight:700;font-size:14.5px;color:#fff}
.f-val{position:absolute;left:886px;font-family:"Montserrat",sans-serif;font-size:13.5px;line-height:22px;color:#fff}
.social{position:absolute;top:2829px;width:28px;height:28px;border-radius:50%;border:2.5px solid #fff}
.copyright{left:162px;top:2874px;font-family:"Poppins",sans-serif;font-size:18px;color:#fff}
</style>
</head>
<body>

<header class="site-header">
  <div class="abs brand">Brindel Asset Development</div>
  <nav class="nav">
    <a style="left:627px">Home</a>
    <a style="left:702px">About</a>
    <a style="left:777px">Services</a>
    <a style="left:867px">Properties</a>
  </nav>
  <div class="abs btn-contact">Contact</div>
</header>

<section class="abs hero">
  <svg width="1200" height="600" viewBox="0 0 1200 600" style="position:absolute;left:0;top:0">
    <defs>
      <linearGradient id="heroLeft" x1="0" y1="0" x2="1" y2="1">
        <stop offset="0" stop-color="#3f5677"/>
        <stop offset=".45" stop-color="#6b7585"/>
        <stop offset=".75" stop-color="#b59a6c"/>
        <stop offset="1" stop-color="#8a6d45"/>
      </linearGradient>
      <linearGradient id="heroRight" x1="0" y1="0" x2="1" y2="1">
        <stop offset="0" stop-color="#c9d2dc"/>
        <stop offset=".5" stop-color="#5d86b0"/>
        <stop offset="1" stop-color="#1f5d8f"/>
      </linearGradient>
    </defs>
    <rect width="1200" height="600" fill="url(#heroLeft)" role="img" aria-label="Photograph of modern apartment buildings against a blue sky"/>
    <path d="M1200 0 L1200 600 L390 600 C560 570 640 480 720 380 C800 260 900 200 1015 160 Z" fill="#fff"/>
    <path d="M1200 0 L1015 160 L1200 95 Z" fill="#fff"/>
    <path d="M1200 95 L1128 150 L1200 145 Z" fill="#4b6fc8"/>
    <path d="M745 490 C700 510 670 560 700 600 L745 600 Z" fill="#4b6fc8"/>
    <path d="M745 170 L1200 140 L1200 600 L745 600 Z" fill="url(#heroRight)" role="img" aria-label="Photograph of a glass high-rise seen from below"/>
  </svg>
  <div class="abs hero-title">TRANSFORMING PROPERTIES,<br>MAXIMIZING RETURNS</div>
  <div class="abs hero-sub">Partner with Brindel Asset Development to optimize<br>your real estate portfolio</div>
  <div class="abs btn-read">Read More</div>
</section>

<div class="abs team-backdrop" role="img" aria-label="Soft decorative backdrop behind the team photo"></div>
<div class="abs team-photo" role="img" aria-label="Photograph of the team gathered around a laptop in an office"></div>
<h2 class="abs h2 team-title">MEET OUR TEAM</h2>
<p class="abs team-text">Our experienced team is dedicated to helping passive real estate investors maximize their portfolio's potential. With a focus on multi-family apartment development, we're committed to delivering exceptional results</p>
<div class="abs btn-square">GET STARTED</div>

<section class="abs expertise">
  <svg width="1200" height="472" style="position:absolute;left:0;top:0" aria-hidden="true">
    <path d="M16 472 V160 Q16 0 180 0 H520 Q680 0 680 160 V472" fill="#3b67b6"/>
    <path d="M105 472 V240 Q105 90 250 90 H450 Q595 90 595 240 V472" fill="#3561b0"/>
  </svg>
</section>
<h2 class="abs exp-title">OUR EXPERTISE IN MULTI-FAMILY<br>APARTMENT&nbsp; DEVELOPMENT</h2>
<p class="abs exp-text">We specialize in developing and repositioning properties to increase cash flow and optimize performance. Our services are designed to help you achieve your real estate goals</p>

<div class="service-card" style="left:696px;top:1228px">
  <svg width="64" height="64" viewBox="0 0 64 64" fill="none" stroke="#fff" stroke-width="2.2" stroke-linejoin="round"><rect x="10" y="10" width="16" height="26"/><rect x="30" y="4" width="22" height="22"/><circle cx="36" cy="40" r="7"/><path d="M4 50 H20 L34 56 L58 44 M4 58 H20"/></svg>
</div>
<div class="service-label" style="left:686px;top:1361px">Passive Real Estate<br>Investing</div>

<div class="service-card" style="left:880px;top:1228px">
  <svg width="68" height="68" viewBox="0 0 68 68" fill="none" stroke="#fff" stroke-width="2.2" stroke-linejoin="round"><circle cx="34" cy="34" r="26" stroke-dasharray="8 4"/><path d="M18 36 L34 22 L50 36 M23 32 V52 H45 V32"/><rect x="30" y="40" width="8" height="12"/></svg>
</div>
<div class="service-label" style="left:869px;top:1360px">Property Development</div>

<div class="service-card" style="left:696px;top:1424px">
  <svg width="64" height="64" viewBox="0 0 64 64" fill="none" stroke="#fff" stroke-width="2.2" stroke-linejoin="round"><rect x="28" y="6" width="28" height="40"/><path d="M34 14 H50 M34 20 H50 M34 26 H50"/><path d="M8 36 L24 24 L40 36 M12 33 V58 H36 V33"/><circle cx="14" cy="12" r="4"/><circle cx="14" cy="22" r="4"/></svg>
</div>
<div class="service-label" style="left:690px;top:1555px">Property Management</div>

<div class="service-card" style="left:880px;top:1424px">
  <svg width="66" height="66" viewBox="0 0 66 66" fill="none" stroke="#fff" stroke-width="2.2" stroke-linejoin="round"><path d="M10 33 A23 23 0 0 1 52 20 M56 33 A23 23 0 0 1 14 46"/><path d="M52 10 V20 H42 M14 56 V46 H24"/><circle cx="33" cy="33" r="11"/><path d="M28 34 L32 38 L39 29"/></svg>
</div>
<div class="service-label" style="left:872px;top:1555px">Asset Optimization</div>

<h2 class="abs h2 pf-title">OUR PORTFOLIO</h2>
<p class="abs pf-text">We specialize in developing and repositioning properties to increase cash flow and optimize performance.<br>Our services are designed to help you achieve your real estate goals</p>

<div class="photo" style="left:168px;top:1836px;width:363px;height:154px;background:linear-gradient(180deg,#c7d8ee,#7d8ea6 70%,#2d3645)" role="img" aria-label="Photograph of a contemporary dark-clad house"></div>
<div class="photo" style="left:172px;top:2001px;width:363px;height:197px;background:linear-gradient(180deg,#c4c7c6 0%,#b7aea0 40%,#8a4a3a 70%,#3a2a26)" role="img" aria-label="Photograph of a city skyline with a tall round tower"></div>
<div class="photo" style="left:540px;top:1836px;width:306px;height:359px;background:linear-gradient(160deg,#c8d0e4,#8f9bbd 60%,#5e6a8a)" role="img" aria-label="Photograph of a curved apartment building with balconies"></div>
<div class="photo" style="left:854px;top:1837px;width:164px;height:358px;background:linear-gradient(180deg,#a8b1ba,#6f7883 50%,#3e4650)" role="img" aria-label="Photograph of a steel high-rise tower"></div>
<div class="arrow" style="left:118px;top:1999px"><svg width="14" height="14" viewBox="0 0 14 14"><path d="M9 2 L4 7 L9 12" fill="none" stroke="#fff" stroke-width="2"/></svg></div>
<div class="arrow" style="left:1040px;top:1999px"><svg width="14" height="14" viewBox="0 0 14 14"><path d="M5 2 L10 7 L5 12" fill="none" stroke="#fff" stroke-width="2"/></svg></div>

<section class="abs cta" role="img" aria-label="Photograph of a city skyline at dusk behind a dark overlay"></section>
<h2 class="abs cta-title">READY TO TRANSFORM YOUR PORTFOLIO?</h2>
<p class="abs cta-text">Contact us to learn more about our services and how we can help you maximize your real estate portfolio</p>
<div class="abs btn-pill">GET STARTED TODAY</div>

<footer class="abs site-footer">
  <svg width="1200" height="346" style="position:absolute;left:0;top:0" aria-hidden="true">
    <path d="M975 346 V160 Q975 20 1110 20 H1200 V346" fill="#5283cf"/>
    <path d="M1035 346 V190 Q1035 80 1140 80 H1200 V346" fill="#4a78c8"/>
  </svg>
</footer>
<div class="abs footer-brand">Brindel Asset Development</div>
<div class="f-head" style="left:698px;top:2653px">QUICK LINK</div>
<div class="f-link" style="top:2706px">About</div>
<div class="f-link" style="top:2744px;left:698px">services</div>
<div class="f-link" style="top:2782px;left:698px">Properties</div>
<div class="f-link" style="top:2824px">contact us</div>
<div class="f-head" style="left:884px;top:2653px">CONTACT US</div>
<div class="f-label" style="top:2703px">ADDRESS</div>
<div class="f-val" style="top:2723px">Lorem ipsum dolor sit amet,<br>consectetur adipiscing elit</div>
<div class="f-label" style="top:2786px">EMAIL ADDRESS</div>
<div class="f-val" style="top:2805px">info@brindelasset.com</div>
<div class="f-label" style="top:2846px;left:888px">GIVE US A CALL</div>
<div class="f-val" style="top:2868px">+1 555 0142 600</div>
<div class="social" style="left:157px" aria-label="Social link"></div>
<div class="social" style="left:219px" aria-label="Social link"></div>
<div class="social" style="left:283px" aria-label="Social link"></div>
<div class="abs copyright">2024 @brindel. All rights reserved</div>

</body>
</html>
```